Recruitment of Brackwell Staffing for the UK market

I want a website for the UK market to attract businesses and companies to come to us for Philipine labour. We want an information site that gives all information on what we do and how we can recruit Philippine labour.
This is a recruitment site for companies to contact us with their requirements for skilled workers coming from the Philipines over to the UK to work.

Target Market(s)

Uk Companies and businesses who want Philipine skilled workers

Industry/Entity Type

REcruitment

Coding

Coded - Design and coding required

Number of Pages Required

5+ page

Font styles to use
Sans Serif

Colors
0054AA
0677BA
7BADD7
CADEEF
E8F1F8
0094D4
00A9DD
6FCCEA
C7EBF8
E9F6FB
EE7325
F08F49
F5BC92
FAE3D3
FDF4ED
EB3D1F
EC4F4E
F09395
F8D3D4
FCEDEE

Requirements
Must have
• Look professional and corperate with drop down menus for Home ,about, services,articles. training , contact us
Nice to have
• Look at Tolvery recruitment- https://tolveryrecruitment.example.co.uk/. This is my current site - https://www.brackwellstaffing.example.com/
Should not have
• Cartoons or silly pictures , needs to be corperate looking

```html
<!DOCTYPE html>
<html lang="en">
<head>
<meta charset="utf-8">
<title>Brackwell Staffing — Skilled Philippine Workers for UK Companies</title>
<link href="https://fonts.googleapis.com/css2?family=Oswald:wght@500;600;700&family=Poppins:wght@400;500;600&display=swap" rel="stylesheet">
<style>
:root{
  --brand-red:#9c2a2b;
  --brand-red-soft:#c98f90;
  --ink:#222222;
  --text:#555555;
  --muted:#8a8a8a;
  --paper:#ffffff;
  --grey-band:#c4c4c4;
  --footer:#2a2a2a;
  --footer-line:#4a4a4a;
}
*{margin:0;padding:0;box-sizing:border-box}
html,body{width:1200px;height:4332px;overflow:hidden}
body{position:relative;background:var(--paper);font-family:'Poppins',sans-serif;color:var(--text)}
.abs{position:absolute}
h1,h2,h3,h4,.oswald{font-family:'Oswald',sans-serif;color:var(--ink);text-transform:uppercase}

/* header */
.site-header{left:0;top:0;width:1200px;height:88px;background:var(--paper)}
.brand{left:92px;top:26px;font-family:'Poppins',sans-serif;font-weight:600;font-size:24px;color:var(--brand-red);display:flex;align-items:center;gap:10px}
.brand .mark{width:16px;height:16px;background:var(--brand-red)}
.main-nav{right:90px;top:32px;display:flex;gap:20px;font-size:14px;font-weight:600;color:var(--ink)}
.main-nav span.drop::after{content:"";display:inline-block;width:5px;height:5px;border-right:1.5px solid var(--ink);border-bottom:1.5px solid var(--ink);transform:rotate(45deg);margin-left:5px;position:relative;top:-3px}

/* hero */
.hero{left:0;top:88px;width:1200px;height:752px;background:linear-gradient(180deg,#3d4a5c 0%,#6c7480 45%,#8d8470 75%,#5e5a4a 100%)}
.hero-title{left:0;top:300px;width:1200px;text-align:center;color:#fff;font-size:58px;line-height:63px;font-weight:600}

/* about */
.about-photo{left:92px;top:888px;width:510px;height:587px;background:linear-gradient(135deg,#d9dde2,#9aa3ab 60%,#5f6870);clip-path:polygon(0 0,100% 0,100% 94%,0 100%)}
.eyebrow{left:654px;top:980px;font-family:'Oswald',sans-serif;font-size:16px;color:var(--brand-red-soft);text-transform:uppercase}
.about-title{left:654px;top:1005px;font-size:50px;line-height:54px;font-weight:600}
.about-copy{left:654px;top:1122px;width:420px;font-size:14.5px;line-height:27px}
.btn-dark{left:654px;top:1293px;width:152px;height:43px;background:var(--ink);color:#fff;font-family:'Oswald',sans-serif;font-size:13px;display:flex;align-items:center;justify-content:center;clip-path:polygon(8% 0,100% 0,92% 100%,0 100%)}

.section-title{left:0;width:1200px;text-align:center;font-size:50px;font-weight:600}
.services{left:260px;top:1575px;display:flex;gap:12px}
.service-card{width:163px;height:210px;background:var(--paper);box-shadow:0 12px 30px rgba(0,0,0,.12);clip-path:polygon(0 0,100% 0,100% 92%,0 100%);padding:36px 0 0 34px}
.service-card.active{background:var(--brand-red)}
.service-card svg{width:60px;height:60px;margin-left:0}
.service-card h4{font-size:17px;line-height:22px;font-weight:500;margin-top:18px}
.service-card.active h4{color:#fff}

/* training */
.training{left:0;top:1863px;width:1200px;height:617px;background:radial-gradient(circle at 70% 40%,#34466a,#141c2e 70%);clip-path:polygon(0 0,100% 0,100% 86%,0 62%)}
.training-band{left:0;top:2300px;width:1200px;height:180px;background:var(--grey-band);clip-path:polygon(0 0,100% 74%,100% 100%,0 22%)}
.training-title{left:92px;top:2000px;font-size:116px;line-height:130px;font-weight:700;color:#fff}
.training-sub{left:92px;top:2130px;font-size:17px;color:#fff;font-weight:500}
.play{left:970px;top:2353px;width:140px;height:140px;border-radius:50%;background:var(--brand-red);display:flex;align-items:center;justify-content:center}

.lead{left:0;top:2540px;width:1200px;text-align:center;font-family:'Oswald',sans-serif;font-size:17px;line-height:24px;color:var(--ink);font-weight:500}
.steps{left:90px;top:2635px;display:flex;gap:18px}
.step-card{width:242px;height:262px;background:var(--paper);box-shadow:0 12px 30px rgba(0,0,0,.1);clip-path:polygon(0 0,100% 0,100% 93%,0 100%);padding:34px 18px 0 20px}
.step-card svg{width:80px;height:80px}
.step-card h4{font-size:17px;font-weight:500;margin-top:14px}
.step-card p{font-size:13px;line-height:18px;margin-top:4px}
.step-card .more{font-size:12px;color:var(--muted);margin-top:6px;text-transform:uppercase;font-weight:500}

.workers-photo{left:210px;top:2955px;width:400px;height:435px;background:linear-gradient(180deg,#f5f5f5,#e7cfa1 40%,#c98a3d 75%,#f5f5f5)}
.info-list{left:655px;top:3075px;width:360px}
.info-list h4{font-size:17px;font-weight:500}
.info-list p{font-size:14px;line-height:22px;margin:4px 0 46px}

.news{left:96px;top:3520px;display:flex;gap:14px}
.news-card{position:relative;width:327px;height:352px;clip-path:polygon(0 0,100% 0,100% 86%,0 100%)}
.news-card .meta{position:absolute;left:34px;top:268px;color:#fff;font-size:13px}
.news-card .meta b{display:block;font-family:'Oswald',sans-serif;font-size:17px;font-weight:500;margin-top:4px}

/* footer */
.footer-band{left:0;top:3870px;width:1200px;height:180px;background:var(--grey-band);clip-path:polygon(0 100%,100% 0,100% 100%)}
.site-footer{left:0;top:3920px;width:1200px;height:412px;background:var(--footer);clip-path:polygon(0 100%,0 68%,100% 0,100% 100%)}
.footer-brand{left:230px;top:4118px;font-size:24px;font-weight:600;color:var(--brand-red);display:flex;align-items:center;gap:10px}
.footer-brand .mark{width:16px;height:16px;background:var(--brand-red)}
.footer-contact{left:565px;top:4080px;color:#fff}
.footer-contact h4{color:#fff;font-size:20px;font-weight:500;margin-bottom:12px}
.footer-contact li{list-style:none;display:flex;gap:10px;font-size:12.5px;line-height:17px;margin-bottom:9px;color:#ddd}
.footer-contact svg{flex:none;width:10px;height:12px;margin-top:2px}
.socials{left:820px;top:4115px;display:flex;gap:10px}
.socials span{width:30px;height:30px;border-radius:50%;background:#3c3c3c;border:1px solid #555}
.footer-rule{left:95px;top:4278px;width:1010px;height:1px;background:var(--footer-line)}
.copyright{left:0;top:4294px;width:1200px;text-align:center;color:#fff;font-size:12px;font-weight:500}
.to-top{left:1120px;top:4250px;width:38px;height:38px;border-radius:50%;background:#444;display:flex;align-items:center;justify-content:center}
</style>
</head>
<body>

<header class="site-header abs">
  <div class="brand abs"><span class="mark"></span>Brackwell Staffing</div>
  <nav class="main-nav abs">
    <span>Home</span><span class="drop">About Us</span><span class="drop">Services</span><span class="drop">Articles</span><span class="drop">Training</span><span>Contact us</span>
  </nav>
</header>

<section class="hero abs" role="img" aria-label="Construction workers in hard hats looking up at tall buildings under construction"></section>
<svg class="abs" style="left:0;top:700px" width="1200" height="140" viewBox="0 0 1200 140">
  <polygon points="0,140 1200,0 1200,28 140,140" fill="#c4c4c4"/>
  <polygon points="0,140 1200,28 1200,140" fill="#fff"/>
</svg>
<h1 class="hero-title abs">Recruiting and placing<br>skilled Philippine workers<br>into UK companies</h1>

<div class="about-photo abs" role="img" aria-label="Smiling chef in white uniform preparing a dish in a kitchen"></div>
<div class="eyebrow abs">About Company</div>
<h2 class="about-title abs">What the business<br>is about</h2>
<p class="about-copy abs">We source skilled workers directly from the Philippines to work in the UK. With offices , training locations and specialist recruiters we can find the highest quality individuals to add value and resources to any UK buisness. We delivery quality based on vast experience over a number of years.</p>
<div class="btn-dark abs">VIEW MORE</div>

<h2 class="section-title abs" style="top:1495px">Our Services</h2>
<div class="services abs">
  <div class="service-card">
    <svg viewBox="0 0 60 60" fill="none" stroke="#9c2a2b" stroke-width="2"><path d="M30 34V18M30 24c-8-2-10-10-10-10 8 0 10 6 10 10zm0 0c8-2 10-10 10-10-8 0-10 6-10 10z"/><path d="M6 40h10l10 4h12l12-8M6 48h14l18 2 16-10"/></svg>
    <h4>Agriculture</h4>
  </div>
  <div class="service-card">
    <svg viewBox="0 0 60 60" fill="none" stroke="#9c2a2b" stroke-width="2"><path d="M18 10h24l-6 12H24z"/><path d="M30 22v10"/><rect x="8" y="38" width="44" height="8" rx="4"/><circle cx="14" cy="52" r="3"/><circle cx="30" cy="52" r="3"/><circle cx="46" cy="52" r="3"/><rect x="24" y="30" width="12" height="8"/></svg>
    <h4>Food<br>processing</h4>
  </div>
  <div class="service-card active">
    <svg viewBox="0 0 60 60" fill="none" stroke="#fff" stroke-width="2"><path d="M16 24a14 14 0 0 1 28 0z"/><path d="M12 24h36M30 8v2"/><rect x="10" y="30" width="40" height="22"/><path d="M10 40h40M22 30v22"/></svg>
    <h4>Hospitality<br>and catering</h4>
  </div>
  <div class="service-card">
    <svg viewBox="0 0 60 60" fill="none" stroke="#9c2a2b" stroke-width="2"><path d="M16 56V10M10 16h44M16 10l-6 6M20 16v10M44 16v14"/><rect x="38" y="30" width="12" height="10"/><rect x="8" y="48" width="16" height="8"/><path d="M34 56V44h18v12"/></svg>
    <h4>Building and<br>construction</h4>
  </div>
</div>

<section class="training abs" role="img" aria-label="Blacksmith with a hammer shaping glowing metal on an anvil in a dark workshop"></section>
<div class="training-band abs"></div>
<h2 class="training-title abs">Training</h2>
<div class="training-sub abs">BRACKWELL STAFFING</div>
<div class="play abs"><svg width="28" height="30" viewBox="0 0 28 30"><polygon points="2,0 28,15 2,30" fill="#fff"/></svg></div>

<h2 class="section-title abs" style="top:2465px">Working Together</h2>
<p class="lead abs">We recruit the finest talent available with our dedicated 200 strong team. Our<br>centres are highlighted in red dots on the map.</p>
<div class="steps abs">
  <div class="step-card">
    <svg viewBox="0 0 80 80" fill="none" stroke="#9c2a2b" stroke-width="2"><circle cx="46" cy="32" r="24"/><circle cx="46" cy="32" r="17"/><circle cx="46" cy="27" r="6"/><path d="M36 42c2-6 18-6 20 0"/><path d="M28 50L10 68l4 4 18-18"/></svg>
    <h4>What we do</h4>
    <p>Our company has been estabilished in the Philippines for over 20 years</p>
    <div class="more">Read more</div>
  </div>
  <div class="step-card">
    <svg viewBox="0 0 80 80" fill="none" stroke="#9c2a2b" stroke-width="2"><path d="M8 14l16 16M72 66L56 50M20 26l16 16 8-2 10 10 6-6-22-22-6 2-6-6"/><path d="M30 34l-6 6 4 4 6-6M36 40l-6 6 4 4 6-6M42 46l-6 6 4 4 6-6"/></svg>
    <h4>How we help</h4>
    <p>Our company has been estabilished in the Philippines for over 20 years</p>
  </div>
  <div class="step-card">
    <svg viewBox="0 0 80 80" fill="none" stroke="#9c2a2b" stroke-width="2"><path d="M72 8L14 40l18 6 6 18z"/><path d="M72 8L32 46M18 58l-8 8M24 64l-6 6M12 52l-6 6"/></svg>
    <h4>Where to start</h4>
    <p>Our company has been estabilished in the Philippines for over 20 years</p>
  </div>
  <div class="step-card">
    <svg viewBox="0 0 80 80" fill="none" stroke="#9c2a2b" stroke-width="2"><rect x="28" y="10" width="46" height="32"/><path d="M28 10l23 18 23-18"/><path d="M14 34c-8 8-2 26 14 36l8-8-8-8-6 4c-4-4-6-8-6-14l6-4-4-10z"/></svg>
    <h4>Contact us today</h4>
    <p>Our company has been estabilished in the Philippines for over 20 years</p>
  </div>
</div>

<div class="workers-photo abs" role="img" aria-label="Group of four construction workers in hard hats and overalls holding tools"></div>
<div class="info-list abs">
  <h4>UK skilled workers list</h4>
  <p>The UK government since brexit have developed a new system based on points...</p>
  <h4>Sponsor licence</h4>
  <p>If you have areas of your business that meet the entry requirements...</p>
  <h4>Recruitment timeline</h4>
  <p>Brief us on the job profiles – this is passed on to our teams in the Philippines.</p>
</div>

<h2 class="section-title abs" style="top:3440px">Latest News</h2>
<div class="news abs">
  <div class="news-card" role="img" aria-label="Construction worker in safety harness on a building site" style="background:linear-gradient(180deg,#a9b3bb,#6d7377 60%,#4e4f4c)">
    <div class="meta">22-02-2023<b>SOME HEADING HERE</b></div>
  </div>
  <div class="news-card" role="img" aria-label="Worker in hard hat tying steel reinforcement bars" style="background:linear-gradient(180deg,#8fb1d6,#5b6671 55%,#3c3f42)">
    <div class="meta">22-02-2023<b>SOME HEADING HERE</b></div>
  </div>
  <div class="news-card" role="img" aria-label="Nurse holding a clipboard in a hospital ward" style="background:linear-gradient(180deg,#e8ecef,#9fbcc0 55%,#4f7f86)">
    <div class="meta">22-02-2023<b>SOME HEADING HERE</b></div>
  </div>
</div>

<div class="footer-band abs"></div>
<footer class="site-footer abs"></footer>
<div class="footer-brand abs"><span class="mark"></span>Brackwell Staffing</div>
<div class="footer-contact abs">
  <h4>Contact us</h4>
  <ul>
    <li><svg viewBox="0 0 10 12"><path d="M5 0a4 4 0 0 1 4 4c0 3-4 8-4 8S1 7 1 4a4 4 0 0 1 4-4z" fill="#b33"/></svg><span>Larchmere Court, Fenwick Road,<br>Dunholt DH4 7 United Kingdom</span></li>
    <li><svg viewBox="0 0 10 12"><path d="M2 1l2 2-1 2c1 2 2 3 4 4l2-1 1 2-2 2C4 11 0 6 1 2z" fill="#b33"/></svg><span>07700 900418</span></li>
    <li><svg viewBox="0 0 10 12"><rect x="0" y="3" width="10" height="7" fill="#b33"/><path d="M0 3l5 4 5-4" stroke="#2a2a2a" fill="none"/></svg><span>sales@brackwellstaffing.example.com</span></li>
  </ul>
</div>
<div class="socials abs"><span></span><span></span><span></span><span></span></div>
<div class="footer-rule abs"></div>
<div class="copyright abs">© Copyright 2023 &nbsp;| All Right Reserveds</div>
<div class="to-top abs"><svg width="10" height="6" viewBox="0 0 10 6"><path d="M1 5l4-4 4 4" stroke="#fff" stroke-width="1.5" fill="none"/></svg></div>

</body>
</html>
```